Flyer Design

I need a nice professional flyer design to use for advertising my lawn/snow removal business. Flyers I am using are 5.47"x4.21". I've attached a flyer I found online that I liked. Just wanting something creative and professional. The images of the logos I attached are of the original logo design, and the new color design we are using. There is also a mockup of our tshirt design to give you an idea of the actual color on the tshirt, since the jpeg logo isn't exactly accurate on color.
Things I need on the flyer in no particular order:
"Snow is coming"
"Don't Wait Until It's TOO LATE!"
"Free Estimates"
Services offered
"Commercial/Residential"
"Snow Plowing"
"Snow Blowing"
"Snow Shoveling"
"Ice Removal"
"Salting/Sanding"
"Fully Licensed and Insured"
"Available and ON CALL 24/7"
"Seasonal Packages Available"
"CALL NOW TO RESERVE"

```html
<!DOCTYPE html>
<html lang="en">
<head>
<meta charset="utf-8">
<title>Snow Removal Flyer</title>
<link href="https://fonts.googleapis.com/css2?family=Noto+Serif:wght@400;700&family=Open+Sans:wght@700;800&display=swap" rel="stylesheet">
<style>
  :root {
    --page-bg: #eeeeec;
    --card-light: #e4e4e4;
    --card-mid: #cfcfcf;
    --snow-white: #f7f8fa;
    --snow-shade: #d9dde2;
    --brand-orange: #f26f12;
    --ink: #141414;
    --paper-white: #ffffff;
  }
  * { box-sizing: border-box; margin: 0; padding: 0; }
  html, body { width: 1200px; height: 1199px; overflow: hidden; background: var(--page-bg); }
  body { position: relative; font-family: "Noto Serif", Georgia, serif; color: var(--ink); }

  .flyer {
    position: absolute; left: 90px; top: 200px; width: 963px; height: 743px;
    background: radial-gradient(ellipse at 50% 60%, var(--card-light), var(--card-mid));
    box-shadow: 0 4px 14px rgba(0,0,0,.25);
    overflow: hidden;
  }

  .hero-photo {
    position: absolute; left: 150px; top: 0; width: 813px; height: 372px;
    border-radius: 186px 0 0 186px;
    background: linear-gradient(160deg, var(--snow-shade) 0%, var(--snow-white) 45%, var(--paper-white) 100%);
  }

  .brand {
    position: absolute; left: 40px; top: 120px; width: 380px;
    display: flex; align-items: center; gap: 18px;
  }
  .brand-dot { flex: none; width: 70px; height: 70px; border-radius: 50%; background: var(--brand-orange); }
  .brand-name { font-weight: 700; font-size: 38px; line-height: 1.1; color: var(--ink); }

  .headline {
    position: absolute; left: 440px; top: 258px; width: 510px; text-align: center;
  }
  .headline-main { font-size: 58px; font-weight: 400; color: var(--brand-orange); line-height: 1.1; letter-spacing: .5px; }
  .headline-sub { font-size: 27px; font-weight: 700; line-height: 1.2; }

  .services { position: absolute; left: 50px; top: 410px; width: 330px; }
  .services-title { font-size: 37px; font-weight: 700; line-height: 1.2; text-align: center; }
  .services-type { font-size: 23px; font-weight: 700; color: var(--brand-orange); text-align: center; margin-top: 2px; }
  .service-list { list-style: none; margin-top: 12px; padding-left: 36px; }
  .service-list li { display: flex; align-items: center; gap: 20px; font-size: 25px; height: 40.5px; }
  .tick { width: 24px; height: 24px; flex: none; }

  .contact { position: absolute; left: 455px; top: 406px; width: 490px; text-align: center; }
  .contact-line { font-size: 26px; line-height: 32px; }
  .contact-line.on-call { color: var(--brand-orange); font-weight: 700; letter-spacing: .5px; }
  .call-now { font-size: 38px; font-weight: 700; color: var(--brand-orange); margin-top: 22px; line-height: 1.2; }
  .phone-banner { position: relative; width: 448px; height: 82px; margin: 4px auto 0; }
  .phone-banner svg { position: absolute; inset: 0; }
  .phone-number {
    position: relative; line-height: 82px; font-family: "Open Sans", Arial, sans-serif;
    font-weight: 800; font-size: 58px; color: var(--paper-white); letter-spacing: -.5px;
  }
  .packages { font-size: 31px; margin-top: 6px; letter-spacing: .3px; }
</style>
</head>
<body>
  <main class="flyer">
    <div class="hero-photo" role="img" aria-label="Photo of a white pickup truck with a red plow blade clearing a snowy road"></div>

    <div class="brand">
      <span class="brand-dot"></span>
      <span class="brand-name">Frostline Lawn &amp; Landscape</span>
    </div>

    <div class="headline">
      <h1 class="headline-main">SNOW IS COMING</h1>
      <p class="headline-sub">Don't Wait Until It's TOO LATE!</p>
    </div>

    <section class="services">
      <h2 class="services-title">Services Offered</h2>
      <p class="services-type">Commercial - Residential</p>
      <ul class="service-list">
        <li><svg class="tick" viewBox="0 0 24 24"><circle cx="12" cy="12" r="11" fill="var(--brand-orange)"/><path d="M6.5 12.5l4 4 7-8" fill="none" stroke="#fff" stroke-width="3" stroke-linecap="round" stroke-linejoin="round"/></svg>Snow Plowing</li>
        <li><svg class="tick" viewBox="0 0 24 24"><circle cx="12" cy="12" r="11" fill="var(--brand-orange)"/><path d="M6.5 12.5l4 4 7-8" fill="none" stroke="#fff" stroke-width="3" stroke-linecap="round" stroke-linejoin="round"/></svg>Snow Blowing</li>
        <li><svg class="tick" viewBox="0 0 24 24"><circle cx="12" cy="12" r="11" fill="var(--brand-orange)"/><path d="M6.5 12.5l4 4 7-8" fill="none" stroke="#fff" stroke-width="3" stroke-linecap="round" stroke-linejoin="round"/></svg>Snow Shoveling</li>
        <li><svg class="tick" viewBox="0 0 24 24"><circle cx="12" cy="12" r="11" fill="var(--brand-orange)"/><path d="M6.5 12.5l4 4 7-8" fill="none" stroke="#fff" stroke-width="3" stroke-linecap="round" stroke-linejoin="round"/></svg>Ice Removal</li>
        <li><svg class="tick" viewBox="0 0 24 24"><circle cx="12" cy="12" r="11" fill="var(--brand-orange)"/><path d="M6.5 12.5l4 4 7-8" fill="none" stroke="#fff" stroke-width="3" stroke-linecap="round" stroke-linejoin="round"/></svg>Salting/Sanding</li>
      </ul>
    </section>

    <section class="contact">
      <p class="contact-line">Fully Licensed and Insured</p>
      <p class="contact-line on-call">AVAILABLE AND ON CALL 24/7</p>
      <p class="contact-line">Free Estimate</p>
      <p class="call-now">Call Now to Reserve</p>
      <div class="phone-banner">
        <svg viewBox="0 0 448 82" width="448" height="82" aria-hidden="true">
          <polygon points="0,0 448,0 436,41 448,82 0,82 12,41" fill="var(--brand-orange)"/>
        </svg>
        <p class="phone-number">123-456-7890</p>
      </div>
      <p class="packages">Seasonal Packages Available</p>
    </section>
  </main>
</body>
</html>
```